Home Services- Spring Clean Options

Brightfold Services provides a variety of Home Services- focused on cleaning & improving the exterior of the home:

 Power Washing- driveways, sidewalks, patios, decks, fence
 Fence Staining- make fence look new with variety of staining colors
 Gutter cleaning- important to make sure have proper Water Drainage
 Gutter Guard Installation- prevent damage to roof and house by keeping debris out of gutters and water flowing.
 Window Washing- our exterior washing team and reach the highest windows
 Landscape& Patio Lights- highlight areas for beauty and safety
Updates

We are are almost finished. Just please make sure you pay attention to the wording and grammer in Red thx

Target Market(s)

Middle to Upper level Home Owners (especially women)

Industry/Entity Type

Cleaning Services

Font styles to use
Serif
Sans Serif

Requirements
Must have
• Not be Cluttered- Clean friendly, professional look. Focus on the Professional

Info@TryBrightfoldServices.com
845-267-0000
Nice to have
• Pictures of services- these are just examples
Should not have
• Bigger and bolder Services & Specials. Want to Show all the Services we offer but do Not use too much detail- don't want it to look "cluttered"

```html
<!DOCTYPE html>
<html lang="en">
<head>
<meta charset="utf-8">
<title>Brightfold Services – Home Service Flyer</title>
<link href="https://fonts.googleapis.com/css2?family=Montserrat:wght@600;700;800&family=Oswald:wght@500;600&family=Roboto:wght@400;500;700&family=Lato:wght@400&display=swap" rel="stylesheet">
<style>
  :root{
    --green:#5a8f29;
    --green-dark:#3f6e17;
    --blue:#1f7fcf;
    --blue-light:#2b8fde;
    --white:#ffffff;
    --ink:#333333;
    --paper:#ffffff;
  }
  *{margin:0;padding:0;box-sizing:border-box}
  html,body{width:900px;height:1200px;overflow:hidden;background:#f2f2f2}
  .flyer{position:relative;width:900px;height:1200px;overflow:hidden;background:var(--paper);font-family:"Roboto",Arial,sans-serif;color:var(--ink)}

  .hero-panel{position:absolute;left:0;top:0;width:436px;height:418px;background:var(--green);color:var(--white)}
  .brand{position:absolute;left:36px;top:40px;display:flex;align-items:center;gap:16px}
  .brand-square{width:22px;height:22px;background:var(--white)}
  .brand-name{font-family:"Montserrat",sans-serif;font-weight:700;font-size:30px;line-height:1.05;letter-spacing:1px}
  .hero-title{position:absolute;left:34px;top:176px;font-family:"Montserrat",sans-serif;font-weight:800;font-size:72px;line-height:.95;letter-spacing:1px}
  .hero-sub{position:absolute;left:36px;top:322px;font-size:32px;line-height:1.05;font-weight:400}

  .hero-photo{position:absolute;left:436px;top:0;width:464px;height:418px;background:linear-gradient(135deg,#e6e9ee 0%,#c9ced6 55%,#3b5fb0 75%,#b9bec6 100%)}
  .hero-rule{position:absolute;left:0;top:418px;width:900px;height:6px;background:var(--blue-light)}

  .headline{position:absolute;left:36px;top:462px;font-family:"Oswald",sans-serif;font-weight:500;font-size:35px;line-height:1.1;color:var(--blue);text-transform:uppercase;letter-spacing:-.3px;white-space:nowrap;transform:scaleX(.9);transform-origin:left top}
  .subline{position:absolute;left:36px;top:510px;font-weight:700;font-size:23px;color:var(--green);white-space:nowrap}

  .service{position:absolute;width:258px;text-align:center}
  .service-photo{position:relative;width:258px;height:190px;border:2px solid #555}
  .service-label{position:absolute;left:50%;bottom:-4px;transform:translateX(-50%);background:var(--green);color:var(--white);font-weight:500;font-size:19px;line-height:1.05;padding:6px 14px;white-space:nowrap;box-shadow:3px 3px 0 var(--green-dark)}
  .service-desc{margin-top:14px;font-family:"Lato",sans-serif;font-size:14px;line-height:1.3;color:var(--ink)}

  .footer{position:absolute;left:0;top:1108px;width:900px;height:92px}
  .footer-phone{position:absolute;left:32px;top:16px;display:flex;align-items:center;gap:16px;color:var(--white);font-family:"Oswald",sans-serif;font-weight:500;font-size:54px;line-height:1}
  .footer-contact{position:absolute;left:470px;top:8px;display:flex;flex-direction:column;gap:4px;color:var(--white)}
  .footer-line{display:flex;align-items:center;gap:12px;font-weight:700;font-size:22px;line-height:1.15;white-space:nowrap}
  .footer-line.email{font-weight:500;font-size:18px}
</style>
</head>
<body>
<main class="flyer">
  <section class="hero-panel">
    <div class="brand">
      <span class="brand-square"></span>
      <span class="brand-name">BRIGHTFOLD<br>CLEANING</span>
    </div>
    <h1 class="hero-title">HOME<br>SERVICE</h1>
    <p class="hero-sub">Cleaning &amp; improving<br>the exterior of the home</p>
  </section>
  <div class="hero-photo" role="img" aria-label="Cleaner in blue overalls mopping a bright living room floor"></div>
  <div class="hero-rule"></div>

  <h2 class="headline">Brightfold Services provides a variety of home services</h2>
  <p class="subline">Focused on cleaning &amp; improving the exterior of the home</p>

  <article class="service" style="left:36px;top:556px">
    <div class="service-photo" role="img" aria-label="Worker power washing a paved lot" style="background:linear-gradient(180deg,#b9c4cf 0%,#8d98a3 45%,#d3d8dc 100%)"><span class="service-label">Power Washing</span></div>
    <p class="service-desc">Driveways, sidewalks, patios,<br>decks, fence</p>
  </article>
  <article class="service" style="left:321px;top:556px">
    <div class="service-photo" role="img" aria-label="Gloved hand staining a white fence" style="background:linear-gradient(90deg,#7b7f86 0%,#e2e4e6 40%,#a7abb1 70%,#3a4050 100%)"><span class="service-label">Fence Staining</span></div>
    <p class="service-desc">Make fence look new with<br>variety of staining colors</p>
  </article>
  <article class="service" style="left:606px;top:556px">
    <div class="service-photo" role="img" aria-label="Worker spraying gutters beside pine trees" style="background:linear-gradient(180deg,#2f8fd0 0%,#5aa7dc 45%,#3d6b3a 80%,#4d4d4d 100%)"><span class="service-label">Gutter cleaning</span></div>
    <p class="service-desc">Important to make sure<br>have proper Water Drainage</p>
  </article>

  <article class="service" style="left:36px;top:828px">
    <div class="service-photo" role="img" aria-label="Worker installing gutter guards on a roof" style="background:linear-gradient(180deg,#9fc2e6 0%,#cfdcea 35%,#3b3d40 65%,#6a6a5a 100%)"><span class="service-label">Gutter Guard<br>Installation</span></div>
    <p class="service-desc">Prevent damage to roof and house<br>by keeping debris out of gutters and<br>water flowing</p>
  </article>
  <article class="service" style="left:321px;top:828px">
    <div class="service-photo" role="img" aria-label="Hand wiping a window with a blue cloth" style="background:linear-gradient(135deg,#e8eef2 0%,#a9d6ee 50%,#3aa5dc 100%)"><span class="service-label">Window Washing</span></div>
    <p class="service-desc">Our exterior washing team can<br>reach the highest windows</p>
  </article>
  <article class="service" style="left:606px;top:828px">
    <div class="service-photo" role="img" aria-label="Evening patio with string lights and trees" style="background:linear-gradient(180deg,#7f97b8 0%,#4f6a4a 45%,#5a3a2c 75%,#2f2a26 100%)"><span class="service-label">Landscape &amp;<br>Patio Lights</span></div>
    <p class="service-desc">Highlight areas for beauty<br>and safety</p>
  </article>

  <footer class="footer">
    <svg width="900" height="92" viewBox="0 0 900 92" style="position:absolute;left:0;top:0">
      <rect x="0" y="0" width="900" height="92" fill="var(--green)"/>
      <polygon points="420,0 900,0 900,76 442,76" fill="var(--blue-light)"/>
    </svg>
    <div class="footer-phone">
      <svg width="36" height="36" viewBox="0 0 24 24" fill="#fff" aria-hidden="true"><path d="M6.6 10.8a15.1 15.1 0 0 0 6.6 6.6l2.2-2.2c.3-.3.7-.4 1-.2 1.1.4 2.3.6 3.6.6.6 0 1 .4 1 1V20c0 .6-.4 1-1 1A17 17 0 0 1 3 4c0-.6.4-1 1-1h3.5c.6 0 1 .4 1 1 0 1.3.2 2.5.6 3.6.1.3 0 .7-.2 1z"/></svg>
      <span>845-267-0000</span>
    </div>
    <div class="footer-contact">
      <div class="footer-line">
        <svg width="22" height="22" viewBox="0 0 24 24" fill="none" stroke="#fff" stroke-width="1.8" aria-hidden="true"><circle cx="12" cy="12" r="10"/><ellipse cx="12" cy="12" rx="4.5" ry="10"/><path d="M2 12h20M4 7h16M4 17h16"/></svg>
        <span>www.brightfoldclean.com</span>
      </div>
      <div class="footer-line email">
        <svg width="22" height="18" viewBox="0 0 24 18" fill="none" stroke="#fff" stroke-width="1.8" aria-hidden="true"><rect x="1" y="1" width="22" height="16" rx="2"/><path d="M1 2l11 8 11-8"/></svg>
        <span>Info@TryBrightfoldServices.com</span>
      </div>
    </div>
  </footer>
</main>
</body>
</html>
```